finlo-welt.de
Zielgruppe
Alle die kein Geld haben :-)
Aufgabenstellung
Unter finlo-welt.de sollen Informationen rund um Kredite, Kreditkarten, Bonvia usw. entstehen. Diese werden dann unter Subdomains wir konto.finlo-welt.de oder kreditkarte.finlo-welt.de laufen. Die Domain finlo-welt.de soll die Hauptdomain werden wofür ein Logo und ein Layout benötigt wird. Auf den einzelnen Seiten sollen später Reporte verkauft werden und relativ viel mit Plunko Werbung gearbeitet werden. Hier ein paar Beipspiele www.zahlwerk-mohnel.biz, www.lumvesta88.de, www.tanne-blau-heft.de, www.nordlicht-mappe-brief.de
Die genannten Seiten sind keine Meisterleistung in Design und sollen nur in etwa Inhalte und die Einbindung von Plunko Adbox wieder geben. Menüpunkte sind immer gleich und werden sein mit den Untertiteln wie bei www.zahlwerk-mohnel.biz.

```html
<!DOCTYPE html>
<html lang="de">
<head>
<meta charset="utf-8">
<title>finlo-welt.de – Startseite</title>
<link href="https://fonts.googleapis.com/css2?family=Arimo:wght@400;700&display=swap" rel="stylesheet">
<style>
  :root {
    --green: #4fa80a;
    --green-dark: #3e8a06;
    --text: #454545;
    --text-strong: #333333;
    --nav: #2f2f2f;
    --page: #ffffff;
    --backdrop-light: #f4f4f4;
    --backdrop-dark: #b9b9b9;
    --rule: #cfcfcf;
    --photo-dark: #2a2112;
    --photo-mid: #6b5532;
    --photo-light: #c9a070;
  }
  * { box-sizing: border-box; margin: 0; padding: 0; }
  html, body { width: 1200px; height: 1200px; overflow: hidden; }
  body {
    font-family: "Arimo", Arial, sans-serif;
    color: var(--text);
    background: linear-gradient(180deg, var(--backdrop-light) 0%, #dedede 45%, var(--backdrop-dark) 100%);
    position: relative;
  }
  .page {
    position: absolute; left: 78px; top: 0; width: 1047px; height: 1200px;
    background: var(--page);
    box-shadow: 0 0 14px rgba(0,0,0,.28);
  }
  .site-header {
    height: 122px;
    background: linear-gradient(180deg, #e9e9e9 0%, #ffffff 70%);
    border-bottom: 2px solid var(--green);
    position: relative;
  }
  .brand {
    position: absolute; left: 38px; top: 16px;
    display: flex; align-items: center; gap: 12px;
    font-size: 50px; font-weight: 700; color: var(--green);
    letter-spacing: -1px;
  }
  .brand-mark { width: 26px; height: 26px; background: var(--green); }
  .main-nav {
    position: absolute; right: 36px; top: 94px;
    display: flex; font-size: 16.5px; font-weight: 700;
  }
  .main-nav a { color: var(--nav); text-decoration: none; padding: 0 22px; border-left: 2px solid var(--green); line-height: 16px; }
  .main-nav a:first-child { border-left: none; }
  .main-nav a.active { color: var(--green); }

  .content { position: absolute; left: 38px; top: 150px; width: 673px; }
  h1, h2 { color: var(--green); font-weight: 700; font-size: 34px; letter-spacing: -0.3px; }
  h1 { margin-bottom: 18px; }
  h2 { margin-bottom: 20px; }
  p { font-size: 17px; line-height: 25px; margin-bottom: 24px; color: var(--text); }
  p strong { color: var(--text-strong); }

  .ad-box { position: relative; border: 1.5px solid var(--green); }
  .ad-box.inline { height: 148px; display: flex; padding: 18px 0 0 27px; margin-top: -2px; }
  .ad { font-size: 14px; line-height: 26px; }
  .ad-box.inline .ad { width: 310px; }
  .ad h3 { color: var(--green); font-size: 19px; font-weight: 700; margin-bottom: 6px; line-height: 24px; }
  .ad .ad-text { color: var(--text); }
  .ad a { color: var(--green-dark); font-weight: 700; font-size: 13px; }
  .ad-label {
    position: absolute; right: -1px; bottom: -1px;
    background: var(--green); color: #fff; font-size: 14px;
    padding: 2px 6px 2px 14px; border-top-left-radius: 10px;
  }
  .ad-label small { font-size: 10px; }

  .hero-photo {
    margin: 42px 0 54px; height: 308px;
    background: radial-gradient(ellipse at 50% 60%, var(--photo-light) 0%, var(--photo-mid) 35%, var(--photo-dark) 80%);
  }
  .cta { text-align: center; font-size: 18px; font-weight: 700; color: var(--green); margin-top: 6px; }
  .cta a { color: var(--green); }

  .sidebar { position: absolute; left: 758px; top: 164px; width: 243px; height: 845px; padding: 18px 16px 0 17px; }
  .sidebar .ad { font-size: 14px; line-height: 27px; margin-bottom: 26px; }
  .sidebar .ad h3 { margin-bottom: 4px; }
</style>
</head>
<body>
<div class="page">
  <header class="site-header">
    <div class="brand"><span class="brand-mark"></span>finlo-welt</div>
    <nav class="main-nav">
      <a class="active" href="#">Startseite</a>
      <a href="#">Bestellen</a>
      <a href="#">Kontakt</a>
      <a href="#">Datenschutz</a>
      <a href="#">Impressum</a>
    </nav>
  </header>

  <main class="content">
    <h1>Willkommen bei finlo-welt.de</h1>
    <p>Lorem ipsum dolor sit amet, consectetuer adipiscing elit, sed diam nonummy nibh euismod tincidunt ut <strong>laoreet dolore</strong> magna aliquam erat volutpat. Ut wisi enim ad minim veniam, quis nostrud.</p>
    <p>Facilisis at vero et accumsan et iusto odio dignissim <strong>qui blandit praesent</strong> luptatum zzril delenit augue duis dolore te feugait nulla facilisi. Lorem ipsum dolor sit amet.</p>

    <aside class="ad-box inline">
      <div class="ad">
        <h3>Kredit online ab 3,59%</h3>
        <div class="ad-text">Individuelle Ratenhöhe und Laufzeit<br>ab 3,59% effektivem Jahreszins.</div>
        <a href="#">www.KreditNova.de</a>
      </div>
      <div class="ad">
        <h3>Endlich Schuldenfrei</h3>
        <div class="ad-text">mit kleinen Raten zum Ziel Sofortkontakt<br>per Mail oder Telefon</div>
        <a href="#">www.rest-schuldenhilfe.de</a>
      </div>
      <span class="ad-label">Plunko <small>-Anzeigen</small></span>
    </aside>

    <div class="hero-photo" role="img" aria-label="Foto: zwei offene Hände halten Münzen, aus denen ein grünes Blatt wächst"></div>

    <h2>Wir können Ihnen helfen</h2>
    <p>Lorem ipsum dolor sit amet, consectetuer adipiscing elit, sed diam nonummy nibh euismod tincidunt ut laoreet dolore magna aliquam erat volutpat.</p>
    <p>Ut wisi enim ad minim veniam, quis nostrud exerci tation ullamcorper suscipit lobortis nisl ut aliquip ex ea commodo consequat. <strong>Duis autem vel eum iriure dolor</strong> in hendrerit in vulputate velit esse molestie consequat.</p>
    <div class="cta">&gt;&gt;&gt; <a href="#">Bestellen Sie direkt hier unseren Ratgeber</a> &lt;&lt;&lt;</div>
  </main>

  <aside class="ad-box sidebar">
    <div class="ad">
      <h3>Kredit online ab 3,59%</h3>
      <div class="ad-text">Individuelle Ratenhöhe und Laufzeit ab 3,59% effektivem Jahreszins.</div>
      <a href="#">www.KreditNova.de</a>
    </div>
    <div class="ad">
      <h3>Sie haben Schulden?</h3>
      <div class="ad-text">Kredite abgelehnt? Geld Probleme? Wir helfen in jeder Situation !</div>
      <a href="#">www.mira-schuldenrat.net</a>
    </div>
    <div class="ad">
      <h3>Kredit mit Sofortzusage</h3>
      <div class="ad-text">€1000-35000 ab 3,9%, 12-84 Monate. Für Angestellte + Selbstständige!</div>
      <a href="#">Varnoly-Kredit.de</a>
    </div>
    <div class="ad">
      <h3>Endlich Schuldenfrei</h3>
      <div class="ad-text">mit kleinen Raten zum Ziel Sofortkontakt per Mail oder Telefon</div>
      <a href="#">www.rest-schuldenhilfe.de</a>
    </div>
    <div class="ad">
      <h3>Sie haben Schulden?</h3>
      <div class="ad-text">Kredite abgelehnt? Geld Probleme? Wir helfen in jeder Situation !</div>
      <a href="#">www.mira-schuldenrat.net</a>
    </div>
    <span class="ad-label">Plunko <small>-Anzeigen</small></span>
  </aside>
</div>
</body>
</html>
```